School Poster

Design so that these can be placed in classrooms across the school.

Attached is another design we have had done. Use a similar theme.

Consider using themes from https://tolvanehs.qx.edu.au/

please edit Binder1 doc.

Target Market(s)

Students and teachers

```html
<!DOCTYPE html>
<html lang="en">
<head>
<meta charset="utf-8">
<title>Before You Ask the Teacher – Classroom Poster</title>
<link rel="stylesheet" href="https://fonts.googleapis.com/css2?family=Montserrat:wght@500;600;700;800&display=swap">
<style>
  :root {
    --navy: #0d3475;
    --navy-deep: #0a2c66;
    --gold: #f6c51b;
    --gold-pale: #fff8e3;
    --sky: #e2edf9;
    --sky-card: #e8eef9;
    --white: #ffffff;
    --stage: #eceef1;
    --red: #e4232f;
  }
  * { box-sizing: border-box; margin: 0; padding: 0; }
  html, body { width: 1200px; height: 946px; overflow: hidden; background: var(--stage); }
  body { font-family: "Montserrat", Arial, sans-serif; color: var(--navy); position: relative; }

  .poster {
    position: absolute; left: 281px; top: 0;
    width: 840px; height: 1245px;
    transform: scale(0.7598); transform-origin: top left;
    background: var(--white); overflow: hidden;
  }
  .abs { position: absolute; }

  /* Header */
  .header-band { left: 0; top: 37px; width: 840px; height: 108px; background: var(--navy); }
  .sky-band { left: 0; top: 145px; width: 840px; height: 87px; background: var(--sky); }
  .school-mark {
    left: 22px; top: 58px; width: 150px; display: flex; align-items: center; gap: 8px;
    color: var(--white); font-weight: 800; font-size: 17px; line-height: 1.1;
  }
  .school-mark .dot { width: 22px; height: 22px; border-radius: 50%; background: var(--gold); flex: none; }
  .title { left: 186px; top: 54px; font-size: 34px; font-weight: 800; color: var(--white); letter-spacing: .5px; }
  .title-rule { left: 186px; top: 94px; width: 620px; height: 3px; background: var(--gold); }
  .subtitle { left: 187px; top: 99px; font-size: 24px; font-weight: 700; color: var(--gold); letter-spacing: .6px; }

  /* Step cards */
  .step-card { top: 257px; width: 228px; height: 450px; border: 2px solid var(--navy); border-radius: 6px; background: var(--white); }
  .step-icon {
    top: 187px; width: 140px; height: 140px; border-radius: 50%;
    border: 7px solid var(--navy); background: var(--white);
    display: flex; align-items: center; justify-content: center;
  }
  .icon-fill { width: 92px; height: 92px; border-radius: 50%; background: radial-gradient(circle, #fde59a 0%, #dfe8f6 75%); }
  .step-num {
    top: 190px; width: 40px; height: 40px; border-radius: 50%; background: var(--navy);
    color: var(--white); font-weight: 800; font-size: 28px; border: 3px solid var(--white);
    display: flex; align-items: center; justify-content: center;
  }
  .step-pill {
    top: 345px; background: var(--navy); color: var(--white); border-radius: 18px;
    font-weight: 800; font-size: 20px; line-height: 22px; text-align: center; padding: 5px 10px; letter-spacing: .3px;
  }
  .step-body { width: 190px; font-size: 15px; line-height: 17px; }
  .step-body .lead { font-weight: 800; margin-bottom: 14px; }
  .step-body ul { list-style: none; }
  .step-body li { position: relative; padding-left: 23px; margin-bottom: 10px; font-weight: 500; }
  .step-body li::before { content: "•"; position: absolute; left: 7px; }
  .step-body .close { font-weight: 500; margin-top: 2px; }
  .value-pill {
    top: 693px; height: 27px; background: var(--navy); color: var(--gold); border-radius: 14px;
    font-weight: 800; font-size: 20px; line-height: 27px; text-align: center; letter-spacing: .5px;
  }

  /* AI section */
  .ai-frame { left: 52px; top: 773px; width: 741px; height: 249px; border: 2px solid var(--navy); border-radius: 6px; }
  .ai-title {
    left: 119px; top: 753px; width: 605px; height: 42px; border-radius: 21px; background: var(--navy);
    color: var(--white); font-weight: 700; font-size: 21px; line-height: 42px; text-align: center; letter-spacing: .8px;
  }
  .rule-box { top: 813px; width: 319px; height: 179px; border-radius: 5px; overflow: hidden; }
  .rule-box.must { left: 82px; background: var(--gold-pale); border: 2px solid var(--gold); }
  .rule-box.help { left: 440px; background: var(--sky-card); border: 2px solid var(--navy); }
  .rule-head { height: 30px; display: flex; align-items: center; gap: 6px; padding-left: 8px; font-weight: 800; }
  .must .rule-head { background: var(--gold); font-size: 14px; }
  .help .rule-head { background: var(--navy); color: var(--gold); font-size: 10px; line-height: 9px; }
  .help .rule-head small { display: block; font-size: 7px; }
  .rule-list { list-style: none; padding: 12px 14px 0 26px; font-size: 12.5px; line-height: 13px; font-weight: 500; }
  .rule-list li { position: relative; padding-left: 20px; margin-bottom: 10px; }
  .rule-list svg { position: absolute; left: 0; top: 0; }

  /* Cannot do */
  .cannot-band { left: 0; top: 1050px; width: 840px; height: 160px; }
  .cannot-pill {
    left: 243px; top: 1037px; width: 357px; height: 40px; border-radius: 20px; background: var(--gold);
    color: var(--navy); font-weight: 800; font-size: 23px; line-height: 40px; text-align: center; letter-spacing: .5px;
  }
  .cannot-item { width: 170px; color: var(--white); font-size: 13.5px; line-height: 17px; text-align: center; font-weight: 500; }
  .cannot-item .x { display: block; margin: 0 auto 14px; }
  .footer-band { left: 0; top: 1209px; width: 840px; height: 36px; background: var(--sky); font-size: 13px; font-weight: 500; text-align: center; line-height: 34px; }
</style>
</head>
<body>
<main class="poster">
  <div class="abs header-band"></div>
  <div class="abs sky-band"></div>
  <div class="abs school-mark"><span class="dot"></span><span>Tolvane<br>SHS</span></div>
  <h1 class="abs title">BEFORE YOU ASK THE TEACHER...</h1>
  <div class="abs title-rule"></div>
  <p class="abs subtitle">TRY THESE STEPS FIRST!</p>

  <!-- Step 1 -->
  <div class="abs step-card" style="left:52px"></div>
  <div class="abs step-icon" style="left:96px"><div class="icon-fill" role="img" aria-label="Icon of a thinking head with a glowing brain"></div></div>
  <div class="abs step-num" style="left:88px">1</div>
  <div class="abs step-pill" style="left:76px;width:182px">THINK FIRST</div>
  <div class="abs step-body" style="left:75px;top:413px">
    <p class="lead">Don’t give up straight away.</p>
    <ul>
      <li>Read the question carefully.</li>
      <li>Identify what you already know.</li>
      <li>Try a strategy you’ve used before.</li>
      <li>give yourself thinking time.</li>
    </ul>
  </div>
  <div class="abs value-pill" style="left:73px;width:188px">WE BELIEVE</div>

  <!-- Step 2 -->
  <div class="abs step-card" style="left:307px"></div>
  <div class="abs step-icon" style="left:350px">
    <svg width="80" height="90" viewBox="0 0 80 90" role="img" aria-label="Clipboard with tick">
      <rect x="8" y="12" width="58" height="72" rx="5" fill="none" stroke="#0d3475" stroke-width="5"/>
      <rect x="24" y="4" width="26" height="14" rx="3" fill="#fff" stroke="#0d3475" stroke-width="5"/>
      <path d="M18 34h36M18 46h36M18 58h22" stroke="#0d3475" stroke-width="4" stroke-linecap="round"/>
      <path d="M44 68l9 9 20-22" fill="none" stroke="#f6c51b" stroke-width="5" stroke-linecap="round" stroke-linejoin="round"/>
    </svg>
  </div>
  <div class="abs step-num" style="left:340px">2</div>
  <div class="abs step-pill" style="left:323px;width:197px">CHECK YOUR<br>SUPPORTS</div>
  <div class="abs step-body" style="left:336px;top:426px">
    <p class="lead">Before asking for help, check:</p>
    <ul>
      <li>Learning goal and success criteria.</li>
      <li>Worked examples.</li>
      <li>Class notes.</li>
      <li>Classroom displays.</li>
      <li>StudyHub resources.</li>
      <li>Task sheet and instructions.</li>
    </ul>
  </div>
  <div class="abs value-pill" style="left:327px;width:188px">WE STRIVE</div>

  <!-- Step 3 -->
  <div class="abs step-card" style="left:566px"></div>
  <div class="abs step-icon" style="left:610px"><div class="icon-fill" role="img" aria-label="Icon of three people talking together"></div></div>
  <div class="abs step-num" style="left:601px">3</div>
  <div class="abs step-pill" style="left:582px;width:197px">ASK 3<br>BEFORE ME</div>
  <div class="abs step-body" style="left:596px;top:426px">
    <p class="lead">Ask three sources before asking the teacher.</p>
    <ul>
      <li>A person (partner or neighbour)</li>
      <li>A place (notes, display, StudyHub)</li>
      <li>A resource (worked example, task sheet)</li>
    </ul>
    <p class="close">Then ask the teacher if you still need help.</p>
  </div>
  <div class="abs value-pill" style="left:587px;width:188px">WE ACHIEVE</div>

  <!-- AI section -->
  <div class="abs ai-frame"></div>
  <h2 class="abs ai-title">USING AI AND OTHER TOOLS RESPONSIBLY</h2>

  <section class="abs rule-box must">
    <div class="rule-head">
      <svg width="18" height="18" viewBox="0 0 18 18"><circle cx="9" cy="9" r="7.5" fill="none" stroke="#0d3475" stroke-width="2"/><path d="M5 9l3 3 5-6" fill="none" stroke="#0d3475" stroke-width="2"/></svg>
      WHAT YOU MUST DO:
    </div>
    <ul class="rule-list">
      <li><svg width="14" height="14" viewBox="0 0 14 14"><rect x="1" y="2" width="10" height="11" fill="none" stroke="#0d3475" stroke-width="1.6"/><path d="M3 7l3 3 7-9" fill="none" stroke="#0d3475" stroke-width="1.8"/></svg>Complete your own work</li>
      <li><svg width="14" height="14" viewBox="0 0 14 14"><rect x="1" y="2" width="10" height="11" fill="none" stroke="#0d3475" stroke-width="1.6"/><path d="M3 7l3 3 7-9" fill="none" stroke="#0d3475" stroke-width="1.8"/></svg>Demonstrate your progress (drafts, notes, planning, revisions)</li>
      <li><svg width="14" height="14" viewBox="0 0 14 14"><rect x="1" y="2" width="10" height="11" fill="none" stroke="#0d3475" stroke-width="1.6"/><path d="M3 7l3 3 7-9" fill="none" stroke="#0d3475" stroke-width="1.8"/></svg>Use feedback to improve your work</li>
      <li><svg width="14" height="14" viewBox="0 0 14 14"><rect x="1" y="2" width="10" height="11" fill="none" stroke="#0d3475" stroke-width="1.6"/><path d="M3 7l3 3 7-9" fill="none" stroke="#0d3475" stroke-width="1.8"/></svg>Demonstrate your understanding of the ideas in your submission</li>
    </ul>
  </section>

  <section class="abs rule-box help">
    <div class="rule-head">
      <svg width="18" height="18" viewBox="0 0 18 18"><circle cx="9" cy="9" r="6" fill="none" stroke="#f6c51b" stroke-width="2"/><circle cx="9" cy="9" r="2" fill="#f6c51b"/></svg>
      <span>WHAT AI CAN HELP YOU DO<small>(WHEN APPROVED BY YOUR TEACHER)</small></span>
    </div>
    <ul class="rule-list">
      <li><svg width="14" height="14" viewBox="0 0 14 14"><rect x="1" y="2" width="10" height="11" fill="none" stroke="#0d3475" stroke-width="1.6"/><path d="M3 7l3 3 7-9" fill="none" stroke="#0d3475" stroke-width="1.8"/></svg>Brainstorm ideas</li>
      <li><svg width="14" height="14" viewBox="0 0 14 14"><rect x="1" y="2" width="10" height="11" fill="none" stroke="#0d3475" stroke-width="1.6"/><path d="M3 7l3 3 7-9" fill="none" stroke="#0d3475" stroke-width="1.8"/></svg>Check spelling, grammar and clarity</li>
      <li><svg width="14" height="14" viewBox="0 0 14 14"><rect x="1" y="2" width="10" height="11" fill="none" stroke="#0d3475" stroke-width="1.6"/><path d="M3 7l3 3 7-9" fill="none" stroke="#0d3475" stroke-width="1.8"/></svg>Read your work aloud using text-to-speech tools</li>
      <li><svg width="14" height="14" viewBox="0 0 14 14"><rect x="1" y="2" width="10" height="11" fill="none" stroke="#0d3475" stroke-width="1.6"/><path d="M3 7l3 3 7-9" fill="none" stroke="#0d3475" stroke-width="1.8"/></svg>Help identify areas for improvement in a draft</li>
    </ul>
  </section>

  <!-- Cannot do -->
  <svg class="abs cannot-band" viewBox="0 0 840 160" preserveAspectRatio="none" aria-hidden="true">
    <path d="M0 38 Q420 -12 840 38 V160 H0 Z" fill="#0d3475"/>
  </svg>
  <h2 class="abs cannot-pill">WHAT YOU CANNOT DO</h2>

  <div class="abs cannot-item" style="left:42px;top:1092px">
    <svg class="x" width="26" height="26" viewBox="0 0 26 26"><circle cx="13" cy="13" r="12" fill="#fff"/><circle cx="13" cy="13" r="10" fill="#e4232f"/><path d="M9 9l8 8M17 9l-8 8" stroke="#fff" stroke-width="2.6" stroke-linecap="round"/></svg>
    <span style="display:block;margin-top:-2px">Submit AI-generated work as your own</span>
  </div>
  <div class="abs cannot-item" style="left:238px;top:1092px">
    <svg class="x" width="26" height="26" viewBox="0 0 26 26"><circle cx="13" cy="13" r="12" fill="#fff"/><circle cx="13" cy="13" r="10" fill="#e4232f"/><path d="M9 9l8 8M17 9l-8 8" stroke="#fff" stroke-width="2.6" stroke-linecap="round"/></svg>
    Copy and paste AI responses without acknowledging or adapting them
  </div>
  <div class="abs cannot-item" style="left:432px;top:1092px">
    <svg class="x" width="26" height="26" viewBox="0 0 26 26"><circle cx="13" cy="13" r="12" fill="#fff"/><circle cx="13" cy="13" r="10" fill="#e4232f"/><path d="M9 9l8 8M17 9l-8 8" stroke="#fff" stroke-width="2.6" stroke-linecap="round"/></svg>
    Use AI tools to complete the whole task for you
  </div>
  <div class="abs cannot-item" style="left:627px;top:1092px">
    <svg class="x" width="26" height="26" viewBox="0 0 26 26"><circle cx="13" cy="13" r="12" fill="#fff"/><circle cx="13" cy="13" r="10" fill="#e4232f"/><path d="M9 9l8 8M17 9l-8 8" stroke="#fff" stroke-width="2.6" stroke-linecap="round"/></svg>
    Submit work that does not demonstrate your understanding
  </div>

  <p class="abs footer-band">If you didn’t create, develop and understand it, it isn’t your work.</p>
</main>
</body>
</html>
```